Premium Lawn fertiliser packaging - Looking for long term designer

*Update at bottom
I need a carefully considered, bold and professional packaging design for my new premium lawn fertiliser product. This contest is for a detailed front of the stand-up pouch packaging and once I’ve chosen a winner, they’ll be asked to create the layout for the back that links to the front as well. I have a full range of additional products that will also need designs and so I'm looking for someone who can do a great job here and who we can work with long term.

The front should include our logo for Pemberly Turf Supply Direct and be titled “Bloom Vigor Max” "Professional Lawn Fertiliser". The spring fertiliser tag line is "Awaken your lawn: Lush Greening, Lasting Health".
Beneath it, it then needs to include some important usage information and the key benefits along with some suitable graphic.

Key information to include:

Apply March - June
Treats 35-50 m2
16-3-8
+2%MgO + 1% Fe + 2.9% CaO (this is the chemical makeup of the fertiliser and needs to be fairly prominent. If you look at other professional fertiliser packaging, you'll see how it needs to compare).

Key features:
Premium fertiliser, used by professionals
Advanced greening with micro-nutrient complex
Dual action Nitrogen: Instant green boost & continuous feed for 3 months
Child & pet safe

Our brand colours are purple and green. Purple = #592999, Green = 3cb64a / 81d742 / 4d9d44

I think these colours look great against a white background.

Please make sure you look at our website as well to get an idea of our brand: www.pemberlyturfsupply.co.uk

To help, I've attached images of competitors fertiliser packaging that I like the look of. I'm not looking for you to copy but just see what type of thing appeals to me, the standard I'm expecting and what I need to compete against....

In addition, I have also attached some potential images you may wish to try using in your design, although please feel free to use your own if you have something better. For the moment, the images are 'preview' images, but once I decide on a design and we agree on the correct image, I will download and send over a fully licensed version.

*** Update*** When submitting your design, can you submit it in 2 formats: The first as a fully printed custom stand-up pouch and the second as a full-size label stuck onto a standup pouch (whatever colour you think is right for your design - choose white if you are not sure). To explain, I've just discovered we won't be able to get full custom bags printed in time for the first run and so we will have to opt for the design to be printed on labels and fixed onto bags. I therefore need to choose a design that works in both formats as both a label on a standup pouch as well as a fully printed pouch. Many thanks.

Target Market(s)

Domestic home-owners

Industry/Entity Type

Lawn care. NOT AGRICULTURE OR FARMING

Font styles to use
Sans Serif

Requirements
Must have
• Presented in 2 formats - see update at bottom of description
Nice to have
• I quite like designs against a white background, although I’m open to other ideas as well.
Should not have
• Please do not include any people or faces in the design. The text should be solid in colour, so no graduated colour fill in the text or outline text. Please avoid over-busy or cluttered designs.

```html
<!DOCTYPE html>
<html lang="en">
<head>
<meta charset="utf-8">
<title>Bloom Vigor Max – Professional Lawn Fertiliser</title>
<link rel="stylesheet" href="https://fonts.googleapis.com/css2?family=Montserrat:wght@700;800&family=Oswald:wght@400;500&family=Quicksand:wght@400;500;700&family=Open+Sans:wght@400;600&display=swap">
<style>
  :root{
    --stage:#8f8f8f;
    --green:#5e9f2e;
    --green-dark:#3f7a22;
    --green-text:#2f5e1c;
    --leaf:#81d742;
    --purple:#4b2a98;
    --white:#ffffff;
    --silver:#c9cccf;
    --ink:#3a3a3a;
  }
  *{box-sizing:border-box;margin:0;padding:0}
  html,body{width:1200px;height:720px;overflow:hidden;background:var(--stage)}
  .canvas{position:relative;width:1200px;height:720px}
  .pouch-front{
    position:absolute;left:440px;top:15px;width:320px;height:690px;
    background:var(--white);overflow:hidden;border-radius:4px;
  }
  .hero-photo{
    position:absolute;left:0;top:0;width:320px;height:380px;
    background:linear-gradient(180deg,#5f7a45 0%,#8b8a6a 22%,#a99a80 42%,#8a7660 58%,#4a3526 74%,#2e2119 100%);
  }
  .brand-card{
    position:absolute;left:150px;top:12px;width:158px;height:116px;
    background:var(--white);border-radius:6px;
    display:flex;flex-direction:column;align-items:center;justify-content:center;gap:6px;
  }
  .brand-dot{width:22px;height:22px;border-radius:50%;background:var(--leaf)}
  .brand-name{
    font-family:"Quicksand",sans-serif;font-weight:700;color:var(--green-text);
    font-size:15px;line-height:1.15;text-align:center;
  }
  .claim{
    position:absolute;left:136px;top:196px;color:var(--white);
    font-family:"Open Sans",sans-serif;font-size:11.5px;line-height:1.55;letter-spacing:.2px;
  }
  .claim strong{font-family:"Montserrat",sans-serif;font-weight:800;font-size:11.5px}
  .feature-icons{position:absolute;left:30px;top:178px;width:40px}
  .feature-icons svg{display:block;margin-bottom:12px}
  .title-band{position:absolute;left:0;top:330px;width:320px;height:120px}
  .product-title{
    position:absolute;left:0;top:366px;width:320px;text-align:center;color:var(--white);
    font-family:"Montserrat",sans-serif;font-weight:800;font-size:28px;line-height:1;letter-spacing:-.5px;
  }
  .product-type{
    position:absolute;left:0;top:402px;width:320px;text-align:center;color:var(--white);
    font-family:"Open Sans",sans-serif;font-weight:600;font-size:11px;line-height:1;letter-spacing:1px;
  }
  .tagline{
    position:absolute;left:0;top:464px;width:320px;text-align:center;color:var(--green-text);
    font-family:"Quicksand",sans-serif;font-size:13px;line-height:1.35;
  }
  .tagline strong{font-family:"Montserrat",sans-serif;font-weight:700;font-size:13px;display:block}
  .benefits{position:absolute;left:26px;top:518px;width:170px;list-style:none}
  .benefits li{
    position:relative;padding-left:12px;margin-bottom:9px;
    font-family:"Quicksand",sans-serif;font-size:9.5px;line-height:1.3;color:var(--ink);
  }
  .benefits li::before{content:"\221A";position:absolute;left:0;top:-1px;color:var(--green-text);font-size:11px}
  .benefits b{color:var(--green-text);font-weight:700}
  .usage-box{
    position:absolute;left:204px;top:514px;width:116px;height:88px;
    background:var(--purple);border-radius:6px 0 0 6px;color:var(--white);
    font-family:"Oswald",sans-serif;font-size:12px;line-height:1.2;text-align:center;
    display:flex;flex-direction:column;justify-content:center;
  }
  .usage-box hr{border:0;border-top:1px solid rgba(255,255,255,.8);width:70px;margin:5px auto}
  .spec-bar{position:absolute;left:0;top:630px;width:320px;height:60px;background:var(--green)}
  .spec-bar .weight-panel{
    position:absolute;right:0;top:0;width:86px;height:60px;background:var(--green-dark);
    clip-path:polygon(14px 0,100% 0,100% 100%,0 100%);
  }
  .analysis{
    position:absolute;left:20px;top:8px;width:200px;text-align:center;color:var(--white);
    font-family:"Oswald",sans-serif;font-weight:500;font-style:italic;font-size:16px;line-height:1.3;
  }
  .net-weight{
    position:absolute;right:10px;top:0;color:var(--white);
    font-family:"Oswald",sans-serif;font-weight:500;font-size:36px;line-height:60px;
  }
  .net-weight small{font-size:15px}
</style>
</head>
<body>
<div class="canvas">
  <div class="pouch-front">
    <div class="hero-photo" role="img" aria-label="Photograph of a young seedling growing out of dark crumbly soil, blurred field behind"></div>

    <div class="brand-card">
      <span class="brand-dot"></span>
      <p class="brand-name">Pemberly<br>Turf Supply Direct</p>
    </div>

    <div class="feature-icons" aria-hidden="true">
      <svg width="34" height="34" viewBox="0 0 36 36" fill="none" stroke="#fff" stroke-width="1.6">
        <path d="M18 3l12 5v9c0 8-5 13-12 16C11 30 6 25 6 17V8z"/>
        <path d="M12 18l4 4 8-8"/>
      </svg>
      <svg width="34" height="34" viewBox="0 0 36 36" fill="none" stroke="#fff" stroke-width="1.4">
        <circle cx="10" cy="10" r="4"/>
        <path d="M10 2v2M10 16v2M2 10h2M16 10h2"/>
        <rect x="24" y="3" width="5" height="22" rx="2.5"/>
        <circle cx="26.5" cy="29" r="4"/>
        <path d="M6 24c2 2-2 4 0 6M11 24c2 2-2 4 0 6"/>
      </svg>
      <svg width="34" height="34" viewBox="0 0 36 36" fill="none" stroke="#fff" stroke-width="1.4">
        <path d="M30 18a12 12 0 0 1-21 8M6 18a12 12 0 0 1 21-8"/>
        <path d="M27 4v6h-6M9 32v-6h6"/>
        <path d="M18 25c-4-3-4-8 0-12 4 4 4 9 0 12zM18 25v-6"/>
      </svg>
    </div>

    <p class="claim"><strong>PREMIUM FERTILISER,</strong><br>USED BY PROFESSIONALS</p>

    <svg class="title-band" viewBox="0 0 320 120" aria-hidden="true">
      <polygon points="0,20 160,0 320,20 320,98 160,120 0,98" fill="var(--silver)"/>
      <polygon points="0,27 160,7 320,27 320,90 160,112 0,90" fill="var(--green)"/>
    </svg>
    <h1 class="product-title">BLOOM VIGOR MAX</h1>
    <p class="product-type">PROFESSIONAL LAWN FERTILISER</p>

    <p class="tagline">AWAKEN YOUR LAWN:<strong>LUSH GREENING, LASTING HEALTH</strong></p>

    <ul class="benefits">
      <li>Advanced greening with micro-nutrient complex.</li>
      <li><b>Dual action Nitrogen:</b> Instant green boost &amp; continuous feed for 3 months.</li>
      <li>Child &amp; pet safe</li>
    </ul>

    <div class="usage-box">
      <span>TREATS<br>35-50 M2</span>
      <hr>
      <span>APPLY<br>MARCH - JUNE</span>
    </div>

    <div class="spec-bar">
      <div class="weight-panel"></div>
      <p class="analysis">16-3-8 +2 % MGO<br>+ 1 % FE + 2,9 % CAO</p>
      <p class="net-weight">10<small>KG</small></p>
    </div>
  </div>
</div>
</body>
</html>
```